Need a clean & modern homepage for an education site + opportunity for longer term work

Thanks for viewing our project. We are excited about this new website and we hope that we might build a relationship with designers as we work on this project. I provided quite a few details and requirements to help you more quickly create a design that meets our needs.
Who we are:
We are a website that discusses the importance of college accreditation and provides a directory of college programs.
What we need:
A homepage that meets the below requirements and is inspired by the examples provided
Definition of accredited:
ac·cred·it·ed [uh-kred-i-tid] adj.
1. officially recognized as meeting the essential requirements, as of academic excellence: accredited schools.
2. provided with official credentials, as by a government: an accredited diplomatic representative.
3. accepted as authoritative: an accredited theory.
Overall look and feel for the homepage:
- Clean, simple and modern
- Limited (or zero) pictures
- Utilize color blocks with text
- A trend seems to be longer vertical length homepages with lots of whitespace. I generally like this trend as long as the page is not way to tall.
Inspirations: Sites that have a similar look and feel to what I need.
http://lernvista.org/
http://www.campusmetrix.com/colleges/orlen-university/
http://quietmarrow.org/
http://www.velmoratalent.com/
http://www.pluvo.com/
http://sketches.zumo.com/
Items to be included on the homepage. Details below on each item.
- Top navigation
- Logo: Please leave a blank area for a logo. The logo has not been designed.
- Simple graphic/color block at the top that highlights a definition of “Accredited” – the definition should be formatted like it is being copy/pasted from a dictionary.
- Space for a video and small (50 word) written description of the video. You can use placeholder text.
- One section with 3 Paragraphs of content (each paragraph around 100 words) with a header at the top. You can use placeholder text but please create the formatting. At the end of the 3 paragraphs please have a “Read More” Note this shouldn't be 3 separate paragraphs with three read mores - it is 3 paragraphs with one read more at the end.
- An area with the header “Search Colleges by State” that has anchor text links to all 50 states.
Top navigation:
- Home
- States – with a subnav dropdown that includes all 50 US states.
- Programs – with a subnav dropdown that includes program titles (list below)
- Degrees - with a subnav dropdown that includes 5 degree levels (list below)
- Accreditation – no subnav
- Rankings – no subnav
- Resources – no subnav
Footer
- Link to about us, privacy, and a copyright www.url.com
Programs List for sub navigation
Accounting
Art
Bible
Business
Criminal Justice
Design
Engineering
English
Law
LPN to RN
Management
Math
MBA
MPH
Medical Assisting
Military
Nursing
Occupational Therapy
Paralegal
Psychology
Pharmacy
RN to BSN
Radiology
Social Work
Sonography
Degrees list for sub navigation
Certificate
Associate
Bachelors
Masters
PhD
Thanks so much - looking forward to working with you!

```html
<!DOCTYPE html>
<html lang="en">
<head>
<meta charset="utf-8">
<title>Accreditation Homepage</title>
<link href="https://fonts.googleapis.com/css2?family=Mulish:wght@400;600;700;800&display=swap" rel="stylesheet">
<style>
:root{
  --white:#ffffff;
  --navy:#1c3a6e;
  --nav-grey:#8a8f96;
  --top-blue:#2a9ad6;
  --green:#4cb848;
  --green-dark:#3ea63b;
  --green-soft:#8fd35a;
  --grey-bg:#ebebeb;
  --card-text:#555a60;
  --ink:#3a3f45;
  --sky:#5bc0eb;
  --blue:#2fb0e3;
  --blue-light:#55c4ea;
  --footer:#1f8bcc;
  --footer-deep:#1670ad;
  --def-box:rgba(96,196,200,.78);
}
*{box-sizing:border-box;margin:0;padding:0}
html,body{width:722px;height:1200px;overflow:hidden;background:var(--white)}
body{font-family:"Mulish",sans-serif;position:relative;color:var(--ink)}
.abs{position:absolute}

/* header */
.top-rule{left:0;top:0;width:722px;height:4px;background:var(--top-blue)}
.site-header{left:0;top:4px;width:722px;height:49px;background:var(--white)}
.logo{left:78px;top:20px;font-size:14px;font-weight:700;color:var(--navy);letter-spacing:.3px}
.social{left:530px;top:8px;display:flex;gap:9px}
.social span{width:14px;height:14px;border-radius:50%;background:var(--green);display:block}
.main-nav{left:266px;top:29px;display:flex;gap:0;font-size:10.5px;color:var(--nav-grey)}
.main-nav a{color:inherit;text-decoration:none;margin-right:14px}

/* hero */
.hero{left:0;top:53px;width:722px;height:205px;background:linear-gradient(180deg,#7fd23f 0%,#a6dd6a 55%,#8ed159 100%)}
.hero-art{left:0;top:0;width:722px;height:205px;background:radial-gradient(ellipse at 50% 30%,rgba(60,140,160,.35),rgba(60,140,160,0) 70%)}
.definition{left:167px;top:30px;width:394px;height:88px;background:var(--def-box);padding:10px 14px;color:var(--white);font-weight:800;font-size:12.5px;line-height:16px;text-transform:uppercase;text-align:center;letter-spacing:.3px}
.search-college{left:138px;top:154px;width:240px;height:23px;background:var(--white);border-radius:3px;font-size:11px;color:#666;padding:5px 12px}
.search-state{left:388px;top:154px;width:113px;height:23px;background:var(--white);border-radius:3px;font-size:11px;color:#666;padding:5px 12px}
.search-state svg{position:absolute;right:8px;top:6px}
.search-btn{left:511px;top:154px;width:67px;height:23px;background:var(--top-blue);color:var(--white);font-size:10.5px;font-weight:700;text-align:center;line-height:23px;border-radius:2px}

/* video band */
.video-band{left:0;top:258px;width:722px;height:103px;background:var(--green)}
.video-copy{left:143px;top:18px;width:250px;font-size:9.4px;line-height:10.5px;color:var(--white)}
.watch-btn{left:257px;top:73px;width:99px;height:22px;border:1px solid var(--white);color:var(--white);font-size:12px;text-align:center;line-height:20px}
.arrow{left:362px;top:62px}
.video-thumb{left:439px;top:9px;width:139px;height:91px;background:linear-gradient(135deg,#e3eef5,#b9cfe0)}
.play{left:52px;top:28px;width:32px;height:32px;border-radius:50%;background:var(--top-blue)}
.play svg{position:absolute;left:11px;top:9px}

/* cards */
.cards-zone{left:0;top:361px;width:722px;height:241px;background:var(--grey-bg)}
.band-shadow{left:0;top:0;width:722px;height:12px;background:linear-gradient(180deg,rgba(0,0,0,.12),rgba(0,0,0,0))}
.card{top:36px;width:183px;height:183px;background:var(--white);box-shadow:0 1px 3px rgba(0,0,0,.1)}
.card-icon{left:10px;top:11px;width:34px;height:34px;border:2px solid var(--ink);border-radius:50%}
.card-icon svg{position:absolute;left:5px;top:5px}
.card-title{left:64px;top:14px;font-size:12.5px;font-weight:700;color:var(--ink)}
.card-sub{left:64px;top:28px;font-size:12px;color:#666}
.card-text{left:10px;top:64px;width:163px;height:86px;overflow:hidden;font-size:7.6px;line-height:9.7px;color:var(--card-text);text-align:justify}
.card-more{left:0;top:148px;width:183px;height:23px;background:var(--sky);color:var(--white);font-size:11px;text-align:center;line-height:23px}
.card-more.is-active{background:var(--green)}

/* features */
.features{left:0;top:602px;width:722px;height:381px;background:var(--blue)}
.tab{left:322px;top:-1px}
.feature-icon{left:86px;width:84px;height:70px}
.feature-title{left:183px;font-size:22px;font-weight:700;color:var(--white)}
.feature-text{left:183px;width:472px;font-size:8.6px;line-height:10.4px;color:var(--white);text-align:justify}
.read-more{left:456px;top:350px;width:196px;height:31px;background:var(--blue-light);color:var(--white);font-size:27px;text-align:center;line-height:31px}

/* footer */
.footer{left:0;top:983px;width:722px;height:174px;background:var(--footer)}
.footer-notch{left:337px;top:0}
.foot-head{top:24px;font-size:14px;font-weight:700;color:var(--white)}
.foot-list{top:50px;list-style:none;font-size:9.5px;line-height:10.8px;color:var(--white)}
.foot-rule{top:55px;width:1px;height:100px;background:rgba(255,255,255,.55)}
.bottom-bar{left:0;top:1157px;width:722px;height:43px;background:var(--footer-deep);color:var(--white);font-size:14px}
.bottom-bar span{position:absolute;top:12px}
</style>
</head>
<body>

<div class="abs top-rule"></div>
<header class="abs site-header">
  <div class="abs logo">MY WEBSITE B\NAME</div>
  <div class="abs social" aria-label="Social links"><span></span><span></span><span></span><span></span></div>
  <nav class="abs main-nav">
    <a>Home</a><a>States</a><a>Programs</a><a>Degrees</a><a>Accreditation</a><a>Rankings</a><a>Resources</a>
  </nav>
</header>

<section class="abs hero">
  <div class="abs hero-art" role="img" aria-label="Photo of many raised hands against a bright green background"></div>
  <div class="abs definition">Simple graphic/color block at the top that highlights a definition of “accredited” – the definition should be formatted like it is being copy/pasted from a dictionary.</div>
  <div class="abs search-college">Search Collage</div>
  <div class="abs search-state">State
    <svg width="8" height="11" viewBox="0 0 8 11"><path d="M4 0a4 4 0 0 1 4 4c0 3-4 7-4 7S0 7 0 4a4 4 0 0 1 4-4z" fill="#bbb"/><circle cx="4" cy="4" r="1.5" fill="#fff"/></svg>
  </div>
  <div class="abs search-btn">SEARCH</div>
</section>

<section class="abs video-band">
  <p class="abs video-copy">written description of the videowritten description of the videowritten description of the video written description of the video written description of the video written description of the video written description of the video</p>
  <div class="abs watch-btn">Watch video</div>
  <svg class="abs arrow" width="60" height="34" viewBox="0 0 60 34"><path d="M2 30 C20 30 34 20 50 6" fill="none" stroke="#fff" stroke-width="1.5"/><path d="M40 6 L52 4 L49 15" fill="none" stroke="#fff" stroke-width="1.5"/></svg>
  <div class="abs video-thumb" role="img" aria-label="Video still of a presenter">
    <div class="abs play"><svg width="12" height="14" viewBox="0 0 12 14"><path d="M0 0 L12 7 L0 14z" fill="#fff"/></svg></div>
  </div>
</section>

<section class="abs cards-zone">
  <div class="abs band-shadow"></div>

  <article class="abs card" style="left:73px">
    <div class="abs card-icon"><svg width="20" height="20" viewBox="0 0 20 20"><path d="M0 6 L10 2 L20 6 L10 10z" fill="#3a3f45"/><circle cx="10" cy="14" r="4" fill="none" stroke="#3a3f45" stroke-width="1.6"/></svg></div>
    <div class="abs card-title">Rankingsp</div>
    <div class="abs card-sub">explain small-desc</div>
    <p class="abs card-text">One section with 3 Paragraphs of content (each paragraph around 100 words) with a header at the top. You can use placeholder text but please create the formatting. At the end of the 3 paragraphs please have a “Read More” Note this shouldn't be 3 separate paragraphs with three read mores - it is 3 paragraphs with one read more at the end.</p>
    <div class="abs card-more is-active">Read More</div>
  </article>

  <article class="abs card" style="left:269px">
    <div class="abs card-icon"><svg width="20" height="20" viewBox="0 0 20 20"><circle cx="10" cy="10" r="8" fill="none" stroke="#3a3f45" stroke-width="1.6"/><path d="M2 10h16M10 2c-4 4-4 12 0 16M10 2c4 4 4 12 0 16" fill="none" stroke="#3a3f45" stroke-width="1.2"/></svg></div>
    <div class="abs card-title">Accreditation</div>
    <div class="abs card-sub">explain small-desc</div>
    <p class="abs card-text">One section with 3 Paragraphs of content (each paragraph around 100 words) with a header at the top. You can use placeholder text but please create the formatting. At the end of the 3 paragraphs please have a “Read More” Note this shouldn't be 3 separate paragraphs with three read mores - it is 3 paragraphs with one read more at the end.</p>
    <div class="abs card-more">Read More</div>
  </article>

  <article class="abs card" style="left:468px">
    <div class="abs card-icon"><svg width="20" height="20" viewBox="0 0 20 20"><rect x="2" y="3" width="16" height="4" fill="#3a3f45"/><rect x="3" y="8.5" width="14" height="4" fill="#3a3f45"/><rect x="2" y="14" width="16" height="4" fill="#3a3f45"/></svg></div>
    <div class="abs card-title">Resources</div>
    <div class="abs card-sub">explain small-desc</div>
    <p class="abs card-text">One section with 3 Paragraphs of content (each paragraph around 100 words) with a header at the top. You can use placeholder text but please create the formatting. At the end of the 3 paragraphs please have a “Read More” Note this shouldn't be 3 separate paragraphs with three read mores - it is 3 paragraphs with one read more at the end.</p>
    <div class="abs card-more">Read More</div>
  </article>
</section>

<section class="abs features">
  <svg class="abs tab" width="78" height="28" viewBox="0 0 78 28"><path d="M0 0 H78 C62 0 56 6 50 16 C46 24 32 24 28 16 C22 6 16 0 0 0z" fill="#ebebeb"/><path d="M34 10h10M39 5v10" stroke="#8a8f96" stroke-width="2"/></svg>

  <svg class="abs feature-icon" style="top:38px" viewBox="0 0 84 70"><path d="M4 26 L44 8 L82 26 L44 44z" fill="#fff"/><path d="M22 36 V54 C30 62 58 62 66 54 V36 L44 46z" fill="#fff"/><path d="M76 29 V50" stroke="#fff" stroke-width="3"/></svg>
  <h2 class="abs feature-title" style="top:38px">header at the top</h2>
  <p class="abs feature-text" style="top:70px">One section with 3 Paragraphs of content (each paragraph around 100 words) with a header at the top. You can use placeholder text but please create the formatting. At the end of the 3 paragraphs please have a “Read More” Note this shouldn't be 3 separate paragraphs with three read mores - it is 3 paragraphs with one read more at the end.One section with 3 Paragraphs of content (each paragraph around 100 words) with a header at the top. You can use placeholder text but please create the formatting. At the end of the 3 paragraphs please have a “Read More” Note this shouldn't be 3 separate paragraphs with three read mores - it is 3 paragraphs with one read more at end</p>

  <svg class="abs feature-icon" style="top:140px" viewBox="0 0 84 70"><rect x="18" y="2" width="50" height="32" fill="none" stroke="#fff" stroke-width="3"/><circle cx="22" cy="52" r="6" fill="#fff"/><circle cx="42" cy="52" r="6" fill="#fff"/><circle cx="62" cy="52" r="6" fill="#fff"/><rect x="14" y="60" width="16" height="8" fill="#fff"/><rect x="34" y="60" width="16" height="8" fill="#fff"/><rect x="54" y="60" width="16" height="8" fill="#fff"/></svg>
  <h2 class="abs feature-title" style="top:138px">header at the top</h2>
  <p class="abs feature-text" style="top:170px">One section with 3 Paragraphs of content (each paragraph around 100 words) with a header at the top. You can use placeholder text but please create the formatting. At the end of the 3 paragraphs please have a “Read More” Note this shouldn't be 3 separate paragraphs with three read mores - it is 3 paragraphs with one read more at the end.One section with 3 Paragraphs of content (each paragraph around 100 words) with a header at the top. You can use placeholder text but please create the formatting. At the end of the 3 paragraphs please have a “Read More” Note this shouldn't be 3 separate paragraphs with three read mores - it is 3 paragraphs with one read more at end</p>

  <svg class="abs feature-icon" style="top:236px" viewBox="0 0 84 70"><path d="M4 30 L50 10 L80 24 L34 46z" fill="#fff"/><path d="M4 30 V46 L34 62 L80 40 V24 L34 46z" fill="none" stroke="#fff" stroke-width="3"/><path d="M20 40 V54" stroke="#fff" stroke-width="3"/></svg>
  <h2 class="abs feature-title" style="top:236px">header at the top</h2>
  <p class="abs feature-text" style="top:268px">One section with 3 Paragraphs of content (each paragraph around 100 words) with a header at the top. You can use placeholder text but please create the formatting. At the end of the 3 paragraphs please have a “Read More” Note this shouldn't be 3 separate paragraphs with three read mores - it is 3 paragraphs with one read more at the end.One section with 3 Paragraphs of content (each paragraph around 100 words) with a header at the top. You can use placeholder text but please create the formatting. At the end of the 3 paragraphs please have a “Read More” Note this shouldn't be 3 separate paragraphs with three read mores - it is 3 paragraphs with one read more at end</p>

  <div class="abs read-more">Read More</div>
</section>

<footer class="abs footer">
  <svg class="abs footer-notch" width="20" height="14" viewBox="0 0 20 14"><path d="M2 2 H18 L10 12z" fill="#fff"/></svg>
  <h3 class="abs foot-head" style="left:75px">Programs</h3>
  <h3 class="abs foot-head" style="left:411px">Degrees</h3>
  <h3 class="abs foot-head" style="left:510px"><svg width="13" height="13" viewBox="0 0 13 13" style="vertical-align:-1px;margin-right:4px"><circle cx="5" cy="5" r="3.8" fill="none" stroke="#fff" stroke-width="2"/><path d="M8 8 L12 12" stroke="#fff" stroke-width="2.2"/></svg>Colleges by State</h3>

  <ul class="abs foot-list" style="left:78px"><li>Accounting</li><li>Art</li><li>Bible</li><li>Business</li><li>Criminal Justice</li><li>Design</li><li>Education</li><li>Engineering</li><li>English</li></ul>
  <div class="abs foot-rule" style="left:175px"></div>
  <ul class="abs foot-list" style="left:198px;top:52px"><li>Accounting</li><li>Art</li><li>Bible</li><li>Business</li><li>Criminal Justice</li><li>Design</li><li>Education</li><li>Engineering</li><li>English</li></ul>
  <div class="abs foot-rule" style="left:285px"></div>
  <ul class="abs foot-list" style="left:305px;top:56px"><li>Accounting</li><li>Art</li><li>Bible</li><li>Business</li><li>Criminal Justice</li><li>Design</li><li>Education</li><li>Engineering</li><li>English</li></ul>
  <div class="abs foot-rule" style="left:394px"></div>
  <ul class="abs foot-list" style="left:413px;top:56px"><li>Accounting</li><li>Art</li><li>Bible</li><li>Business</li><li>Criminal Justice</li><li>Design</li><li>Education</li><li>Engineering</li><li>English</li></ul>
  <div class="abs foot-rule" style="left:501px"></div>
  <ul class="abs foot-list" style="left:523px;top:56px"><li>Accounting</li><li>Art</li><li>Bible</li><li>Business</li><li>Criminal Justice</li><li>Design</li><li>Education</li><li>Engineering</li><li>English</li></ul>
</footer>

<div class="abs bottom-bar">
  <span style="left:62px">copyright@www.url.com</span>
  <span style="left:478px">about us</span>
  <span style="left:559px">privacy</span>
</div>

</body>
</html>
```